"The Craft of Patron Care," fourth edition cover design

Later this year, my publisher, Harold Penmarsh & Daughters, will issue a fourth, substantially revised edition of "The Craft of Patron Care," following the 2016 publication of the third edition and the second and first versions that were issued earlier.

To distinguish this new edition from previous ones, I need a cover design that visually connects and is consistent with what has preceded it, while signaling this is a new and different, worthy of prospective readers/buyers’ attention.

Attached are three different verbal approaches to the new cover; these are NOT MEANT to serve as actual designs, but rather will give you a sense of how language is to be deployed:

The first emphasizes “ART” as the key visual word in the book title;
The second emphasizes “CLIENT SERVICE” as the key visual words in the book title; and,
The third emphasizes just the word "CLIENT" in the book title.

A top-of-the-page is a pre-head that applies to all three versions:
“6 TIMELESS PRINCIPLES FOR ADVERTISING & MARKETING PRO’s
IN AN AI WORLD"

There's a mid-page sub-head for all three versions:
“THE CLASSIC GUIDE,” followed by
“FOURTH EDITION BY GERALD ASHCOMBE

And there's a one-line, bottom-of-the-page designation:
“Foreword by Mae Dunford, Global Executive Creative Director, Starbolt"

The pallette for the previously published third edition was black with red as an accent color on a field of white; I've attached a sample for reference, so you can see how it was executed. For this new fourth edition, I'd like to change the accent color from red to either Wedgewood blue, or British racing green, or an alternative that is assertive and color saturated -- think of primary colors -- that contrast sufficiently with the base of black. As an alternative, you can consider a cover that used either Wedgewood blue, British racing green, or another possibility as a full-bleed field, with copy content either revered out or surprinted.

Lastly, while the new cover largely is meant to be typographically driven, if you can come up with a visual metaphor that illustrates and builds on the book's title, that would be very helpful. By way of reference, the third edition's book cover attempted to do this by introducing a visual element at the end of the book's title that's meant to represent an artist's paint splatter (although I admit it didn't work as well as it should).

Target Market(s)

Prospective purchasers of the book who might discover copies at a bookstore, but more likely will encounter it through online distributors such as Riverdex, Hartwell & Pike, and Tindall’s.

Industry/Entity Type

Advertising and marketing

Font styles to use
Serif
Sans Serif
Other font styles liked:
• A mix of serif and san-serif typefaces is okay. for the examples I shared, I relieid on "Arial Rounded Bold" but you need not be weeded to this. If you opt to mix in a serif font, I am partial to Cambria as a typeface.

Requirements
Must have
• To achieve the goal of being “connected with but distinct” from previous editions, the new cover should be:  Largely typographic, but displaying a color palette different from the previous editions’ black-plus-red-accent on a canvas of white.  Any new accent color selected for use should be vibrant, strong, and highly saturated; think “British racing green,” “Wedgewood blue,” or their equivalents.  In addition to a powerful, “billboard” approach to type and color, consider other visual metaphors that are likely to engage the readers. The winning cover design will stand out from other books, while connecting with the previously published third edition.
Nice to have
• If you can find way to illustrate the book's title through a visual metaphor, that would be ideal.a
Should not have
• Anything that is frivolous or non-sensical

```html
<!DOCTYPE html>
<html lang="en">
<head>
<meta charset="utf-8">
<title>The Craft of Patron Care — Fourth Edition</title>
<link rel="stylesheet" href="https://fonts.googleapis.com/css2?family=Barlow+Condensed:wght@500;600;700&family=Big+Shoulders+Display:wght@800&display=swap">
<style>
  :root {
    --paper: #ffffff;
    --ink: #111111;
    --accent-green: #63e86e;
    --accent-aqua: #55f9cb;
    --accent-blue: #1f5fe0;
    --hand-light: #d8d8d8;
    --hand-dark: #6a6a6a;
  }
  html, body {
    margin: 0;
    padding: 0;
    overflow: hidden;
    background: var(--paper);
  }
  .cover {
    position: relative;
    width: 806px;
    height: 1200px;
    background: var(--paper);
    overflow: hidden;
    font-family: "Barlow Condensed", "Arial Narrow", sans-serif;
    color: var(--ink);
  }
  .right-block {
    position: absolute;
    right: 90px;
    text-align: right;
    text-transform: uppercase;
    margin: 0;
    white-space: nowrap;
  }
  .prehead {
    top: 52px;
    font-size: 31px;
    font-weight: 500;
    line-height: 40px;
  }
  .prehead .lead { color: var(--accent-blue); font-weight: 600; }
  .title-the {
    top: 272px;
    font-size: 86px;
    font-weight: 700;
    line-height: 1;
  }
  .title-word {
    position: absolute;
    left: 70px;
    right: 88px;
    top: 330px;
    display: flex;
    justify-content: space-between;
    font-family: "Big Shoulders Display", "Impact", sans-serif;
    font-weight: 800;
    font-size: 300px;
    line-height: 1;
    transform: scaleY(1.62);
    transform-origin: top center;
    z-index: 1;
  }
  .title-word .l-green { color: var(--accent-green); }
  .title-word .l-aqua { color: var(--accent-aqua); }
  .title-word .l-blue { color: var(--accent-blue); }
  .title-rest {
    top: 768px;
    font-size: 94px;
    font-weight: 600;
    line-height: 1;
  }
  .edition {
    top: 950px;
    font-size: 36px;
    font-weight: 500;
    line-height: 40px;
  }
  .edition .number { color: var(--accent-blue); font-weight: 600; }
  .author {
    top: 1046px;
    font-size: 68px;
    font-weight: 500;
    line-height: 1;
    letter-spacing: 1px;
  }
  .foreword {
    top: 1140px;
    font-size: 21px;
    font-weight: 500;
    line-height: 1;
    text-transform: none;
    letter-spacing: 0.3px;
  }
  .foreword .name { font-weight: 600; }
  .hand {
    position: absolute;
    z-index: 2;
    border-radius: 40px 40px 60px 60px;
    background: linear-gradient(160deg, var(--hand-light), var(--hand-dark));
  }
  .hand-top { left: 338px; top: 200px; width: 170px; height: 70px; transform: rotate(-18deg); }
  .hand-top-fingers { left: 372px; top: 250px; width: 60px; height: 120px; transform: rotate(12deg); }
  .hand-right { left: 630px; top: 470px; width: 70px; height: 170px; transform: rotate(-25deg); }
  .hand-right-arm { left: 660px; top: 590px; width: 140px; height: 70px; transform: rotate(8deg); }
  .hand-left { left: 36px; top: 710px; width: 80px; height: 150px; transform: rotate(-6deg); }
  .hand-left-arm { left: 88px; top: 820px; width: 66px; height: 140px; transform: rotate(-10deg); }
</style>
</head>
<body>
  <main class="cover">
    <p class="right-block prehead">
      <span class="lead">6 Timeless Principles</span><br>
      For Advertising &amp; Marketing Pro’s<br>
      In an AI World
    </p>

    <h1 class="title">
      <span class="right-block title-the">The</span>
      <span class="title-word" aria-label="Craft">
        <span class="l-green">C</span><span class="l-green">R</span><span class="l-aqua">A</span><span class="l-blue">F</span><span class="l-blue">T</span>
      </span>
      <span class="right-block title-rest">Of Patron Care</span>
    </h1>

    <div class="hand hand-top" role="img" aria-label="Black-and-white photo of a hand reaching down to pinch a title letter"></div>
    <div class="hand hand-top-fingers" role="img" aria-label="Fingers of the reaching hand"></div>
    <div class="hand hand-right" role="img" aria-label="Black-and-white photo of a hand pushing a title letter from the right"></div>
    <div class="hand hand-right-arm" role="img" aria-label="Forearm of the right hand"></div>
    <div class="hand hand-left" role="img" aria-label="Black-and-white photo of a hand holding up the first letter"></div>
    <div class="hand hand-left-arm" role="img" aria-label="Forearm of the lower left hand"></div>

    <p class="right-block edition">
      The Classic Guide<br>
      <span class="number">Fourth Edition</span>
    </p>

    <p class="right-block author">Gerald Ashcombe</p>

    <p class="right-block foreword">Foreword by <span class="name">Mae Dunford</span>, Global Executive Creative Director, Starbolt</p>
  </main>
</body>
</html>
```